New lease of life for a tired Country Pub menu, QLD

I need to refresh my menus with updated prices. The menus need to be A4 (the menus are laminated and handed out over the bar. I'd like to include our logo. I will upload our existing menus as well as the new prices. The design should be humble yet stylish if that's ok, please

Target Market(s)

Locals, travellers and workers

Industry/Entity Type

Hospitality, Quintessential Country pub

Font styles to use
Sans Serif

Colors

Designer to choose colors to be used in the design.

Requirements
Must have
• as we run different menus on different nights
Nice to have
• our logo

```html
<!DOCTYPE html>
<html lang="en">
<head>
<meta charset="utf-8">
<title>Marty's Special Parmi Menu – Hotel Calloway</title>
<link rel="stylesheet" href="https://fonts.googleapis.com/css2?family=Anton&family=Montserrat:wght@800;900&family=Montserrat+Alternates:wght@500&display=swap">
<style>
:root{
  --paper:#efefef;
  --ink:#2a2a2a;
  --panel-dark:#2b2b2b;
  --panel-grey:#878787;
  --title-grey:#9c9c9c;
  --beef-title:#3a3a3a;
  --white:#ffffff;
  --red:#e3141f;
  --pill-grey:#777777;
  --rule-line:#5a5a5a;
}
*{margin:0;padding:0;box-sizing:border-box}
html,body{width:831px;height:1200px;overflow:hidden;background:var(--paper)}
.menu{position:relative;width:831px;height:1200px;overflow:hidden;background:var(--paper);font-family:"Montserrat Alternates",sans-serif;color:var(--ink)}
.abs{position:absolute}
.doodles{background:linear-gradient(180deg,#f3f3f3,#e6e6e6)}
.photo{border-radius:50%}
.photo--chicken{left:-3px;top:-46px;width:260px;height:260px;background:radial-gradient(circle at 50% 55%,#9a5a2a,#6b3d1b 60%,#4a2b14)}
.photo--sticky{left:-48px;top:181px;width:230px;height:230px;background:radial-gradient(circle,#a22a1a,#5a130c 62%,#1e1e1e 64%)}
.photo--beef{left:597px;top:-29px;width:280px;height:280px;background:radial-gradient(circle,#5a2a14,#3a1a0c 62%,#2a2a2a 64%)}
.garnish--tomato{left:20px;top:589px;width:54px;height:54px;border-radius:50%;background:radial-gradient(circle at 40% 35%,#ff5a4a,#c8100c)}
.garnish--leaf-right{left:740px;top:360px;width:100px;height:150px;border-radius:50%;background:radial-gradient(ellipse,#7fd13a,rgba(127,209,58,0) 70%)}
.garnish--leaf-left{left:-10px;top:960px;width:90px;height:100px;border-radius:50%;background:radial-gradient(ellipse,#86d63e,rgba(134,214,62,0) 72%)}
.garnish--chili{left:800px;top:790px;width:31px;height:80px;border-radius:40%;background:linear-gradient(160deg,#2f8a2a 0 15%,#d5121a 16%)}
.garnish--pepper{left:750px;top:1100px;width:30px;height:28px;border-radius:50%;background:radial-gradient(circle,#ff6a5a,#d0121a)}
.garnish--tomato-half{left:331px;top:1127px;width:164px;height:164px;border-radius:50%;background:radial-gradient(circle,#ff6a55,#e0281c 70%)}

.brand{left:0;width:831px;top:70px;text-align:center;font-family:"Montserrat",sans-serif;font-weight:900;font-size:21px;line-height:24px;color:var(--ink)}
.headline{left:150px;top:140px}
.price-pill{left:266px;top:328px;height:36px;display:flex;font-family:"Montserrat",sans-serif;font-weight:900;color:var(--white);font-size:17px}
.price-pill__label{background:var(--ink);border-radius:18px 0 0 18px;padding:0 14px 0 18px;display:flex;align-items:center;width:233px}
.price-pill__value{background:#555;margin-left:3px;border-radius:0 18px 18px 0;width:58px;display:flex;align-items:center;padding-left:8px}
.served{left:0;width:831px;top:376px;text-align:center;font-family:"Montserrat",sans-serif;font-weight:900;font-size:14px;color:#3a3a3a}

.panel{top:428px;width:357px;height:800px;border-radius:40px 40px 0 0}
.panel--chicken{left:56px;background:var(--panel-dark)}
.panel--beef{left:419px;background:var(--panel-grey)}
.panel__title{position:absolute;left:36px;top:18px;font-family:"Anton",sans-serif;font-size:54px;line-height:60px;transform:scaleX(.82);transform-origin:left}
.panel--chicken .panel__title{color:var(--title-grey)}
.panel--beef .panel__title{color:var(--white)}
.panel__rule{position:absolute;left:32px;top:100px;width:301px;height:8px;background:repeating-linear-gradient(100deg,var(--white) 0 2px,transparent 2px 5px)}
.panel--beef .panel__rule{background:repeating-linear-gradient(100deg,#2f2f2f 0 2px,transparent 2px 5px)}
.dish{position:absolute;left:36px;width:297px}
.dish__name{font-family:"Montserrat",sans-serif;font-weight:900;font-size:15.5px;line-height:20px;letter-spacing:-.2px}
.panel--chicken .dish__name{color:var(--title-grey)}
.panel--beef .dish__name{color:var(--beef-title)}
.dish__price{position:absolute;right:0;top:0;width:58px;height:19px;border-radius:10px;background:#1f1f1f;border:1px solid #9a9a9a;color:var(--white);font-family:"Montserrat",sans-serif;font-weight:900;font-size:11px;line-height:17px;text-align:center}
.dish__desc{margin-top:8px;width:230px;font-size:13px;line-height:16.8px;color:var(--white)}
.dish__divider{position:absolute;left:36px;width:297px;border-top:1px dotted var(--rule-line)}
.panel--beef .dish__divider{border-color:#a5a5a5}

.nights{top:1144px;height:29px;font-family:"Montserrat",sans-serif;font-weight:900;font-size:13px;color:var(--white);display:flex;align-items:center}
.nights--day{left:234px;width:150px;background:var(--pill-grey);border-radius:15px 0 0 15px;padding-left:19px}
.nights--venue{left:458px;width:150px;background:var(--ink);border-radius:0 15px 15px 0;padding-left:30px}
</style>
</head>
<body>
<main class="menu">
  <div class="abs doodles" style="left:0;top:410px;width:56px;height:790px" role="img" aria-label="Light line doodles of food and produce"></div>
  <div class="abs doodles" style="left:775px;top:380px;width:56px;height:820px" role="img" aria-label="Light line doodles of food and produce"></div>

  <div class="abs photo photo--chicken" role="img" aria-label="Grilled chicken thighs with cherry tomatoes and herbs on a wooden board"></div>
  <div class="abs photo photo--sticky" role="img" aria-label="Bowl of sticky glazed chicken with red capsicum and sesame"></div>
  <div class="abs photo photo--beef" role="img" aria-label="Bowl of braised beef pieces in rich gravy with parsley"></div>
  <div class="abs garnish--leaf-right" role="img" aria-label="Blurred green leaf"></div>

  <div class="abs brand">HOTEL<br>CALLOWAY</div>

  <svg class="abs headline" width="530" height="190" viewBox="0 0 530 190" aria-label="Marty's Special Parmi Menu">
    <text x="265" y="50" text-anchor="middle" font-family="Anton, sans-serif" font-size="46" fill="#3a3a3a" textLength="205" lengthAdjust="spacingAndGlyphs">MARTY'S</text>
    <text x="265" y="175" text-anchor="middle" font-family="Anton, sans-serif" font-size="130" fill="#262626" textLength="456" lengthAdjust="spacingAndGlyphs">PARMI MENU</text>
    <rect x="210" y="57" width="110" height="32" rx="6" fill="#e3141f" stroke="#fff" stroke-width="2"/>
    <text x="265" y="82" text-anchor="middle" font-family="Anton, sans-serif" font-size="24" fill="#fff" textLength="84" lengthAdjust="spacingAndGlyphs">SPECIAL</text>
  </svg>

  <div class="abs price-pill"><span class="price-pill__label">ALL SPECIAL PARMI'S</span><span class="price-pill__value">$30</span></div>
  <p class="abs served">SERVED WITH SALAD OR VEGES AND CHIPS</p>

  <section class="abs panel panel--chicken">
    <h2 class="panel__title">CHICKEN</h2>
    <div class="panel__rule"></div>
    <article class="dish" style="top:133px"><h3 class="dish__name">CHICKEN HAWAII</h3><span class="dish__price">$30.95</span><p class="dish__desc">Tender chicken thigh, napoli sauce, smoked ham off the bone, pineapple, topped with a blend of tasty and mozzarella cheese</p></article>
    <div class="dish__divider" style="top:261px"></div>
    <article class="dish" style="top:277px"><h3 class="dish__name">CHICKEN HOT &amp; SPICY</h3><span class="dish__price">$30.95</span><p class="dish__desc">Tender chicken thigh, napoli &amp; hot sauce, smoked ham off the bone, pepperoni, jalapenos, topped with a blend of tasty and mozzarella cheese</p></article>
    <div class="dish__divider" style="top:409px"></div>
    <article class="dish" style="top:424px"><h3 class="dish__name">AUSSIE CHICKEN PARMI</h3><span class="dish__price">$30.95</span><p class="dish__desc">Tender chicken thigh, napoli sauce &amp; gravy, smoked ham off the bone, sliced beef sausage, topped with a blend of tasty and mozzarella cheese</p></article>
    <div class="dish__divider" style="top:552px"></div>
    <article class="dish" style="top:567px"><h3 class="dish__name">CHICKEN MEATLOVERS</h3><span class="dish__price">$30.95</span><p class="dish__desc">Tender chicken thigh, napoli &amp; bbq sauces, smoked ham off the bone, sliced beef sausage, savoury mince topped with ablend of tasty and mozzarella cheese</p></article>
  </section>

  <section class="abs panel panel--beef">
    <h2 class="panel__title">BEEF</h2>
    <div class="panel__rule"></div>
    <article class="dish" style="top:133px"><h3 class="dish__name">BEEF HAWAII</h3><span class="dish__price">$30.95</span><p class="dish__desc">Freshly crumbed steak, napoli sauce, drizzle of BBQ sauce, smoked ham off the bone, pineapple topped with a blend of tasty and mozzarella cheese</p></article>
    <div class="dish__divider" style="top:261px"></div>
    <article class="dish" style="top:277px"><h3 class="dish__name">BEEF HOT &amp; SPICY</h3><span class="dish__price">$30.95</span><p class="dish__desc">Freshly crumbed steak, napoli &amp; hot sauce, smoked ham off the bone, pepperoni, jalapenos topped with a blend of tasty and mozzarella cheese</p></article>
    <div class="dish__divider" style="top:409px"></div>
    <article class="dish" style="top:424px"><h3 class="dish__name">AUSSIE BEEF PARMI</h3><span class="dish__price">$30.95</span><p class="dish__desc">Freshly crumbed steak, napoli sauce, gravy, smoked ham off the bone, sliced beef sausage topped with a blend of tasty and mozzarella cheese</p></article>
    <div class="dish__divider" style="top:552px"></div>
    <article class="dish" style="top:567px"><h3 class="dish__name">BEEF MEATLOVERS</h3><span class="dish__price">$30.95</span><p class="dish__desc">Freshly crumbed steak, napoli &amp; bbq sauces, smoked ham off the bone, sliced beef sausage, savoury mince topped with a blend of tasty and mozzarella cheese</p></article>
  </section>

  <div class="abs garnish--tomato" role="img" aria-label="Fresh red tomato"></div>
  <div class="abs garnish--leaf-left" role="img" aria-label="Blurred green leaf"></div>
  <div class="abs garnish--chili" role="img" aria-label="Red chilli"></div>
  <div class="abs garnish--pepper" role="img" aria-label="Slice of red capsicum"></div>

  <div class="abs nights nights--day">THURSDAYS</div>
  <div class="abs nights nights--venue">@THE RIDGE</div>
  <div class="abs garnish--tomato-half" role="img" aria-label="Halved tomato"></div>
</main>
</body>
</html>
```